New business card with our logo

we finalized our logo with the help of pixel harbor - now we need a business card using that logo. we are a metal service center providing raw steel and metal products for fabricating, contractors, artists, etc. we have the wording for the back of the card figured out (attached, no deviations from text please), just need help putting it all together.
Contact Information for Business Card
would like the look of steel somehow incorporated in the design ... would like the black part of the logo to be steel or silver color (the S & MORROW)
Font styles to use
Other font styles liked:
- calibri, arial, similar to those, modern looking
Colors
Designer to choose colors to be used in the design.
Requirements
Must have
- Back of card must haves are attached (no deviations from wording please).
- FRONT of card:
- logo
- address
- name
- office tel
- cell
- fax
- website
- address
Nice to have
- incorporate the look of steel or element of steel somehow
- names of the staff on front not in all caps, i.e. Tereza not TEREZA
- this industry is more industrial, not coffee or flower shop so design should be aligned with that
- design should be classic and tasteful

```html
<!DOCTYPE html>
<html lang="en">
<head>
<meta charset="utf-8">
<title>Morrow Steel – Business Card</title>
<link rel="stylesheet" href="https://fonts.googleapis.com/css2?family=Open+Sans:ital,wght@0,400;0,600;0,700;1,400&family=Roboto:wght@400;500&display=swap">
<style>
  :root {
    --bg: #2b2b2d;
    --steel-dark: #5e6064;
    --steel-mid: #8d9095;
    --steel-light: #c4c6c9;
    --steel-shine: #dcdee0;
    --ink: #1f2023;
    --blue: #1a73c9;
    --black-card: #1c1c1e;
    --emboss: #2f3033;
    --emboss-text: #3e3f43;
    --silver: #a9acb1;
  }
  * { box-sizing: border-box; margin: 0; padding: 0; }
  html, body { width: 1200px; height: 900px; overflow: hidden; }
  body {
    background: var(--bg);
    display: flex;
    flex-direction: column;
    align-items: center;
    justify-content: center;
    gap: 56px;
    font-family: "Open Sans", Arial, sans-serif;
  }
  .card {
    width: 620px;
    height: 354px;
    border-radius: 26px;
    position: relative;
    overflow: hidden;
    box-shadow: 0 14px 30px rgba(0,0,0,.45);
  }

  /* FRONT */
  .card--front {
    background: linear-gradient(180deg, var(--steel-dark) 0 12%, transparent 12%),
                linear-gradient(135deg, var(--steel-mid) 0%, var(--steel-shine) 45%, var(--steel-light) 70%, var(--steel-mid) 100%);
  }
  .card--front .edge-strip {
    position: absolute; left: 0; right: 0; bottom: 0; height: 20%;
    background: linear-gradient(90deg, #55575b, #6c6e72 60%, #5a5c60);
  }
  .brand {
    display: flex; align-items: center; gap: 14px;
  }
  .brand__dot {
    width: 34px; height: 34px; border-radius: 50%;
    background: var(--blue);
  }
  .brand__name {
    font-weight: 600; letter-spacing: 1px; text-transform: uppercase;
  }
  .card--front .brand {
    position: absolute; top: 62px; left: 250px;
  }
  .card--front .brand__name { font-size: 32px; color: var(--ink); }

  .person {
    position: absolute; top: 130px; left: 40px; width: 200px;
    text-align: right; font-family: "Roboto", Arial, sans-serif; color: var(--ink);
  }
  .person__name { font-family: "Open Sans", Arial, sans-serif; font-weight: 600; color: var(--blue); font-size: 24px; line-height: 1.1; }
  .person__title { font-size: 15px; margin-bottom: 6px; }
  .person__address { font-size: 16px; line-height: 1.3; }

  .divider {
    position: absolute; left: 258px; top: 134px; width: 2px; height: 128px;
    background: var(--ink);
  }
  .contacts {
    position: absolute; left: 278px; top: 134px;
    list-style: none; font-family: "Roboto", Arial, sans-serif;
    font-size: 19px; color: var(--ink);
  }
  .contacts li { display: flex; align-items: center; gap: 10px; height: 32px; }
  .icon {
    width: 22px; height: 22px; border-radius: 50%;
    background: var(--blue); display: inline-flex; align-items: center; justify-content: center;
    flex: none;
  }
  .icon svg { width: 14px; height: 14px; }
  .website {
    position: absolute; left: 40px; bottom: 22px;
    display: flex; align-items: center; gap: 10px;
    font-family: "Roboto", Arial, sans-serif; font-size: 19px; color: #f2f2f2;
  }

  /* BACK */
  .card--back {
    background: linear-gradient(135deg, #232325, var(--black-card) 60%, #18181a);
    display: flex; flex-direction: column; align-items: center; justify-content: center;
    text-align: center;
  }
  .card--back .brand { margin-bottom: 18px; }
  .card--back .brand__name { font-size: 40px; color: var(--silver); }
  .card--back .brand__dot { width: 42px; height: 42px; }
  .tagline {
    color: var(--emboss-text);
    text-shadow: 0 1px 0 rgba(255,255,255,.05), 0 -1px 0 rgba(0,0,0,.6);
  }
  .tagline--lead { font-size: 22px; text-transform: uppercase; letter-spacing: .5px; }
  .tagline--services { font-size: 15px; text-transform: uppercase; margin-bottom: 12px; }
  .tagline--products { font-size: 16px; line-height: 1.35; }
  .tagline--delivery { font-size: 16px; font-style: italic; margin-top: 12px; }
</style>
</head>
<body>

<section class="card card--front" aria-label="Business card front">
  <div class="edge-strip"></div>

  <div class="brand">
    <span class="brand__dot"></span>
    <span class="brand__name">Morrow Steel</span>
  </div>

  <div class="person">
    <p class="person__name">Dario Kessel</p>
    <p class="person__title">CEO</p>
    <p class="person__address">Your City address<br>Street location<br>NY city, USA</p>
  </div>

  <div class="divider"></div>

  <ul class="contacts">
    <li><span class="icon"><svg viewBox="0 0 14 14"><rect x="4" y="1.5" width="6" height="11" rx="1.2" fill="none" stroke="#fff" stroke-width="1.4"/><circle cx="7" cy="10.5" r=".8" fill="#fff"/></svg></span>123 456 789</li>
    <li><span class="icon"><svg viewBox="0 0 14 14"><path d="M3.5 2.2l2 2-1 1.4a7 7 0 0 0 3.9 3.9l1.4-1 2 2-1.3 1.6C6.7 12 2 7.3 1.9 3.5z" fill="#fff"/></svg></span>123 456 789</li>
    <li><span class="icon"><svg viewBox="0 0 14 14"><rect x="4" y="1.5" width="6" height="4" fill="none" stroke="#fff" stroke-width="1.2"/><rect x="2" y="5.5" width="10" height="5" rx="1" fill="#fff"/><rect x="4" y="9" width="6" height="3.5" fill="#fff" stroke="#1a73c9" stroke-width=".8"/></svg></span>(123)456-789</li>
    <li><span class="icon"><svg viewBox="0 0 14 14"><text x="7" y="11" text-anchor="middle" font-family="Roboto, Arial, sans-serif" font-size="12" font-weight="500" fill="#fff">@</text></svg></span>info@morrowsteel.com</li>
  </ul>

  <div class="website">
    <span class="icon"><svg viewBox="0 0 14 14" fill="none" stroke="#fff" stroke-width="1.1"><circle cx="7" cy="7" r="5.3"/><ellipse cx="7" cy="7" rx="2.3" ry="5.3"/><path d="M1.7 7h10.6M2.6 4.2h8.8M2.6 9.8h8.8"/></svg></span>
    www.yoursite.com
  </div>
</section>

<section class="card card--back" aria-label="Business card back">
  <div class="brand">
    <span class="brand__dot"></span>
    <span class="brand__name">Morrow Steel</span>
  </div>
  <p class="tagline tagline--lead">Metal Service Center</p>
  <p class="tagline tagline--services">Cut • Shear • Punch • Light Fab</p>
  <p class="tagline tagline--products">Structural steel • Stainless &amp; Aluminum<br>Building Components • Rebar • Decking...and more!</p>
  <p class="tagline tagline--delivery">Cut to size, pick-up or Delivered!</p>
</section>

</body>
</html>
```